Fern Guildworks Business Cards

Looking or a business card design for my start-up, called "Fern Guildworks".
Our tagline is "Unleashing the human potential for good through leadership, culture, and education."
Our mission-driven work includes professional/personal development workshops, educational design services, organizational & project management consulting, and coaching services for K-12 schools, organizations, and individuals.
You can check out the website we're building at fernguildworks.com
I select projects from designers who are highly responsive to feedback, engage in dialog about revisions, and provide all root/source documents (so please state in your initial submission that you agree to do so).
Looking forward to seeing your great designs!!
Updates
Hello everyone,
Industry/Entity Type
Building
Requirements
Must have
- Looking for a two sided design that includes our logo (I am uploading two variations that I would like incorporated in .ai format) and website on both sides.
The front side must include:
Logo, Name, Title, Phone, Email, Twitter handle
The back side must include: Logo, @ferngild (our organizational twitter handle)
Nice to have
- I like the rounded corner business cards, but that is not absolutely essential.
Should not have
- Colors beyond those presented in our logo.

```html
<!DOCTYPE html>
<html lang="en">
<head>
<meta charset="utf-8">
<title>Fern Guildworks Business Cards</title>
<link href="https://fonts.googleapis.com/css2?family=Cinzel:wght@400&family=Arvo:wght@400;700&family=Libre+Baskerville&display=swap" rel="stylesheet">
<style>
  :root{
    --stage:#414847;
    --paper:#ffffff;
    --ink-dark:#242122;
    --stone:#aea69d;
    --stone-text:#9c948a;
    --sky:#6ecde2;
    --band-edge:#0a4f69;
    --band-mid:#0aa5d8;
    --body:#3c3a3a;
    --light:#e9e6e2;
  }
  *{margin:0;padding:0;box-sizing:border-box}
  html,body{width:1200px;height:1200px;overflow:hidden;background:var(--stage)}
  .card{position:absolute;top:445px;width:517px;height:310px;overflow:hidden;text-align:center}
  .card--front{left:50px;background:var(--paper)}
  .card--back{left:633px;background:linear-gradient(180deg,#3a3738 0,var(--ink-dark) 30px,var(--ink-dark) 100%)}
  .centered{position:absolute;left:0;right:0}
  .logo-dot{position:absolute;left:50%;width:96px;height:96px;margin-left:-48px;border-radius:50%;background:var(--sky)}
  .wordmark{font-family:"Cinzel",serif;font-weight:400;font-size:26px;line-height:1;color:var(--stone-text);letter-spacing:.2px}
  .card--back .wordmark{color:var(--stone)}
  .pillars{font-family:"Cinzel",serif;font-size:8.5px;letter-spacing:4px;color:var(--stone-text)}
  .pillars span{margin:0 7px}
  .site{font-family:"Libre Baskerville",serif;font-size:7.5px;color:var(--stone-text)}
  .card--back .site{color:var(--light)}
  .tagline{font-family:"Libre Baskerville",serif;font-size:7px;letter-spacing:1.4px;line-height:10px;text-transform:uppercase;color:var(--light)}
  .person{font-family:"Arvo",serif;font-size:12px;color:var(--body)}
  .person strong{font-size:17px;color:var(--sky);font-weight:700}
  .address{font-family:"Arvo",serif;font-size:12px;color:var(--body)}
  .band{position:absolute;left:0;right:0;height:24px;display:flex;align-items:center;justify-content:center;gap:6px;
    background:linear-gradient(180deg,var(--band-edge) 0,var(--band-mid) 40%,var(--band-mid) 60%,var(--band-edge) 100%);
    font-family:"Arvo",serif;font-size:13px;color:#fff}
  .band .item{display:flex;align-items:center;gap:4px;margin:0 3px}
  .chip{width:15px;height:15px;border-radius:2px;background:#2a2a2a;display:inline-flex;align-items:center;justify-content:center}
  .footer-dark{position:absolute;left:0;right:0;bottom:0;height:31px;background:linear-gradient(180deg,#3b3839,var(--ink-dark) 60%)}
  .back-upper{position:absolute;left:0;right:0;top:57px;height:40px;background:linear-gradient(180deg,#4a4748,var(--ink-dark))}
</style>
</head>
<body>
  <section class="card card--front">
    <div class="logo-dot" style="top:38px"></div>
    <div class="centered wordmark" style="top:143px">Fern Guildworks</div>
    <div class="centered pillars" style="top:170px">Leadership<span>|</span>Culture<span>|</span>Education</div>
    <div class="centered site" style="top:190px">www.fernguildworks.com</div>
    <div class="centered person" style="top:208px"><strong>Mara QUILL</strong> Director</div>
    <div class="centered address" style="top:232px">dummy&nbsp; dummy, dummy dummy City, Country</div>
    <div class="band" style="top:255px">
      <span class="item"><span class="chip"><svg width="9" height="11" viewBox="0 0 9 11"><rect x="1.5" y=".5" width="6" height="10" rx="1" fill="none" stroke="#ddd"/><rect x="3" y="2" width="3" height="4" fill="#ddd"/></svg></span>+63 900 555 0142</span>
      <span class="item"><span class="chip"><svg width="11" height="9" viewBox="0 0 11 9"><rect x=".5" y=".5" width="10" height="8" fill="none" stroke="#ddd"/><path d="M.5 .5 5.5 5 10.5 .5" fill="none" stroke="#ddd"/></svg></span>mara@fernguildworks.com</span>
      <span class="item"><span class="chip"></span>@ferngild</span>
    </div>
    <div class="footer-dark"></div>
  </section>

  <section class="card card--back">
    <div class="band" style="top:32px"><span class="item"><span class="chip"></span>@ferngild</span></div>
    <div class="back-upper"></div>
    <div class="logo-dot" style="top:112px"></div>
    <div class="centered wordmark" style="top:217px">Fern Guildworks</div>
    <div class="centered tagline" style="top:241px">Unleashing the human potential for good through<br>leadership, culture, and education</div>
    <div class="centered site" style="top:265px">www.fernguildworks.com</div>
  </section>
</body>
</html>
```